Interior designer needs a gorgeous, chic business card design.

A new, small Interior Design firm needs a business card that is chic, contemporary and elegant. Nothing over the top. My interiors are contemporary classic with an elegant feel to them. I like to use quality finishes and products rather than follow the latest fads. Projects can be anything from Pre start selections, bathrooms, kitchens, bedrooms, custom upholstery, furniture, rugs and art etc. The final design should display quality and an achievable sense of chic. I am open to all colours including black but not limited to this.

```html
<!DOCTYPE html>
<html lang="en">
<head>
<meta charset="utf-8">
<title>Lune Interiors – Business Cards</title>
<link href="https://fonts.googleapis.com/css2?family=Josefin+Sans:wght@300;700&family=Poiret+One&display=swap" rel="stylesheet">
<style>
  :root {
    --page: #ededed;
    --ink: #000000;
    --paper: #ffffff;
    --sage: #98b9b7;
    --rule-light: #ffffff;
  }
  * { margin: 0; padding: 0; box-sizing: border-box; }
  html, body { width: 1200px; height: 805px; overflow: hidden; }
  body { background: var(--page); position: relative; font-family: "Josefin Sans", sans-serif; }

  .card { position: absolute; overflow: hidden; }
  .card--black { left: 44px; top: 48px; width: 271px; height: 689px; background: var(--ink); color: var(--paper); }
  .card--front { left: 352px; top: 53px; width: 480px; height: 328px; background: var(--sage); color: var(--paper); }
  .card--white { left: 373px; top: 418px; width: 459px; height: 329px; background: var(--paper); color: var(--ink); }
  .card--sage { left: 870px; top: 53px; width: 270px; height: 690px; background: var(--sage); color: var(--paper); }

  .wordmark {
    position: absolute;
    font-family: "Josefin Sans", sans-serif;
    font-weight: 300;
    text-transform: uppercase;
    text-align: center;
    line-height: 1;
  }
  .wordmark__name { display: block; font-size: 36px; letter-spacing: 1px; }
  .wordmark__trade { display: block; font-size: 17px; letter-spacing: 1px; margin-top: 6px; }

  .card--black .wordmark { left: 0; right: 0; top: 396px; }
  .card--front .wordmark { left: 0; right: 0; top: 112px; }
  .card--sage .wordmark { left: 0; right: 0; top: 398px; }
  .card--white .wordmark { left: 10px; width: 112px; top: 58px; }
  .card--white .wordmark__name { font-size: 24px; }
  .card--white .wordmark__trade { font-size: 12px; letter-spacing: 0.5px; margin-top: 4px; }

  .divider { position: absolute; height: 3px; background: var(--rule-light); }
  .card--black .divider { left: 17px; width: 237px; top: 535px; }
  .card--sage .divider { left: 14px; width: 241px; top: 537px; }
  .divider--vertical { left: 151px; top: 60px; width: 3px; height: 238px; background: var(--ink); }

  .contact { position: absolute; font-size: 12px; line-height: 15.5px; text-transform: uppercase; white-space: nowrap; }
  .card--black .contact { left: 17px; top: 557px; }
  .card--sage .contact { left: 14px; top: 555px; }
  .card--white .contact { left: 175px; top: 190px; line-height: 16.5px; }
  .contact .label { font-weight: 700; }
  .contact .value { font-family: "Poiret One", sans-serif; font-weight: 400; font-size: 12.5px; }
  .contact .value--web { font-size: 14px; }
</style>
</head>
<body>

  <section class="card card--black">
    <div class="wordmark"><span class="wordmark__name">Lune</span><span class="wordmark__trade">Interiors</span></div>
    <div class="divider"></div>
    <div class="contact">
      <div class="label">Marla Quinn Holloway</div>
      <div><span class="label">(Dip.</span> <span class="value">Interior Design)</span></div>
      <div class="label">Director</div>
      <div><span class="label">Mob:</span> <span class="value">0400318526</span></div>
      <div><span class="label">Email:</span> <span class="value">marla@luneinteriors.com.au</span></div>
      <div><span class="label">Web:</span> <span class="value value--web">www.luneinteriors.com</span></div>
    </div>
  </section>

  <section class="card card--front">
    <div class="wordmark"><span class="wordmark__name">Lune</span><span class="wordmark__trade">Interiors</span></div>
  </section>

  <section class="card card--white">
    <div class="wordmark"><span class="wordmark__name">Lune</span><span class="wordmark__trade">Interiors</span></div>
    <div class="divider divider--vertical"></div>
    <div class="contact">
      <div class="label">Marla Quinn Holloway</div>
      <div><span class="label">(Dip.</span> <span class="value">Interior Design)</span></div>
      <div class="label">Director</div>
      <div><span class="label">Mob:</span> <span class="value">0400318526</span></div>
      <div><span class="label">Email:</span> <span class="value">marla@luneinteriors.com.au</span></div>
      <div><span class="label">Web:</span> <span class="value value--web">www.luneinteriors.com</span></div>
    </div>
  </section>

  <section class="card card--sage">
    <div class="wordmark"><span class="wordmark__name">Lune</span><span class="wordmark__trade">Interiors</span></div>
    <div class="divider"></div>
    <div class="contact">
      <div class="label">Marla Quinn Holloway</div>
      <div><span class="label">(Dip.</span> <span class="value">Interior Design)</span></div>
      <div class="label">Director</div>
      <div><span class="label">Mob:</span> <span class="value">0400318526</span></div>
      <div><span class="label">Email:</span> <span class="value">marla@luneinteriors.com.au</span></div>
      <div><span class="label">Web:</span> <span class="value value--web">www.luneinteriors.com</span></div>
    </div>
  </section>

</body>
</html>
```